W need a Menu Board designed for a" make your own poke bowl" and Sushi Menu. We would like our logo & Colors to be intergraded with the menu . Also will need to be able to adjust the pricing in the future as needed.

```html
<!DOCTYPE html>
<html lang="en">
<head>
<meta charset="UTF-8">
<title>Tidewell Fish Market — Sushi Menu Board</title>
<link href="https://fonts.googleapis.com/css2?family=Archivo:wght@700&family=Didact+Gothic&family=Cabin:wght@500&display=swap" rel="stylesheet">
<style>
  :root {
    --backdrop: #d9e6f3;
    --paper: #ffffff;
    --brand-blue: #0454a8;
    --ink: #1b1b1b;
    --salmon-deep: #e2692a;
    --salmon-light: #f4a36b;
    --rice: #f3eee6;
  }
  * { margin: 0; padding: 0; box-sizing: border-box; }
  html, body { width: 1200px; height: 1020px; overflow: hidden; background: var(--backdrop); }
  .board {
    position: absolute; left: 73px; top: 162px; width: 1054px; height: 721px;
    background: var(--paper); overflow: hidden;
  }
  .board > * { position: absolute; }
  .section-title {
    width: 136px; height: 30px; background: var(--brand-blue); color: #fff;
    font: 700 14.5px/30px "Archivo", sans-serif; letter-spacing: 1px; text-align: center;
  }
  .item-list {
    list-style: none; width: 220px; text-align: center;
    font: 13px/23.4px "Didact Gothic", sans-serif; letter-spacing: 0.9px; color: var(--ink);
  }
  .roll-notes {
    left: 782px; top: 220px; width: 250px; text-align: center;
    font: 500 10px/17.5px "Cabin", sans-serif; color: var(--ink);
  }
  .roll-notes p + p { margin-top: 17px; }
  .footer-band { left: 1px; top: 616px; width: 1053px; height: 105px; background: var(--brand-blue); }
  .tagline {
    left: 353px; top: 651px; width: 400px; text-align: center; color: #fff;
    font: 700 27.5px/1 "Archivo", sans-serif; letter-spacing: 2.5px;
  }
  .brand-name {
    left: 20px; top: 530px; width: 260px; text-align: center; color: var(--brand-blue);
    font: 700 15px/1.2 "Archivo", sans-serif; letter-spacing: 3px;
  }
  .brand-square { left: 138px; top: 500px; width: 24px; height: 24px; }
  .brand-square rect { fill: var(--brand-blue); }
  .photo-top { left: 0; top: 0; width: 281px; height: 330px; }
  .photo-bottom { left: 755px; top: 330px; width: 299px; height: 387px; }
</style>
</head>
<body>
<main class="board">
  <svg class="photo-top" role="img" aria-label="Photo: sushi roll coated in orange roe held by chopsticks, dripping soy sauce" viewBox="0 0 281 330">
    <defs>
      <radialGradient id="roeGlow" cx="0.55" cy="0.5" r="0.55">
        <stop offset="0" stop-color="#f3c79a"/>
        <stop offset="1" stop-color="#e06a22"/>
      </radialGradient>
    </defs>
    <rect x="100" y="70" width="180" height="220" rx="40" fill="url(#roeGlow)"/>
  </svg>

  <svg class="brand-square" viewBox="0 0 24 24" aria-hidden="true"><rect width="24" height="24"/></svg>
  <div class="brand-name">TIDEWELL FISH MARKET</div>

  <div class="section-title" style="left:409px;top:47px">TARTARS</div>
  <ul class="item-list" style="left:367px;top:82px">
    <li>Salmon Tartar $22.99</li><li>Tuna Tartar $24.99</li>
  </ul>

  <div class="section-title" style="left:599px;top:47px">SALADS</div>
  <ul class="item-list" style="left:557px;top:82px">
    <li>Kani Salad $18.99</li>
  </ul>

  <div class="section-title" style="left:409px;top:154px">TOWERS</div>
  <ul class="item-list" style="left:367px;top:189px">
    <li>Tuna Tower $16.99</li><li>Salmon Tower $16.99</li>
  </ul>

  <div class="section-title" style="left:599px;top:154px">TATAKIS</div>
  <ul class="item-list" style="left:557px;top:189px">
    <li>Tuna Tataki</li>
  </ul>

  <div class="section-title" style="left:409px;top:265px">ROLLS</div>
  <ul class="item-list" style="left:367px;top:300px">
    <li>Avocado Roll $7.99</li><li>Cucumber Roll $7.99</li><li>California Roll $9.99</li>
    <li>Veggie Roll $9.99</li><li>Spicy Tuna Roll $9.99</li><li>Salmon Avocado Roll $9.99</li>
    <li>Tuna Roll (small) $9.99</li><li>Salmon Roll (small) $9.99</li>
    <li>Harbor Roll $14.99</li><li>Jetty Roll $15.99</li>
  </ul>

  <div class="section-title" style="left:600px;top:265px">AVOCADOS</div>
  <ul class="item-list" style="left:557px;top:300px">
    <li>(w/ salmon or tuna on top)</li><li>Salmon Avocado $14.99</li><li>Tuna Avocado $14.99</li>
  </ul>

  <div class="section-title" style="left:599px;top:395px">NEGRI</div>
  <ul class="item-list" style="left:557px;top:430px">
    <li>Salmon</li><li>Ahi</li><li>Wahoo</li><li>Hamachi</li><li>Toro</li>
  </ul>

  <div class="roll-notes">
    <p>*Harbor Roll (Inside Out w/ Kani, Cucumber, Avocado,<br>&amp; Tempura Flakes Topped w/ Salmon &amp; Dressed<br>with Eel Sauce)</p>
    <p>*Jetty Roll (Inside Out w/ Kani, Cucumber &amp;<br>Cilantro Topped w/ Hamachi, Jalapeno &amp; Dressed<br>w/ Cilantro Truffle Sauce)</p>
  </div>

  <div class="footer-band"></div>
  <div class="tagline">BEYOND THE BOWL</div>

  <svg class="photo-bottom" role="img" aria-label="Photo: salmon-topped sushi roll held by wooden chopsticks" viewBox="0 0 299 387">
    <defs>
      <linearGradient id="salmonTone" x1="0" y1="0" x2="0.6" y2="1">
        <stop offset="0" stop-color="#f4a36b"/>
        <stop offset="0.6" stop-color="#e9763a"/>
        <stop offset="1" stop-color="#f3eee6"/>
      </linearGradient>
    </defs>
    <rect x="0" y="150" width="210" height="230" rx="40" fill="url(#salmonTone)"/>
  </svg>
</main>
</body>
</html>
```